Silicone product manufacturer needs name card

we are a silicone proudct manufacturer, need a name card.
Updates

Dear All, Pls use the following information for the name card. Maris Odell Marketing Manager Mobile : HK (852) 64839205 : CN (86) 13957204416 Tel : 852-24776150 Fax : 852-28364471 Rm705,7/F, Lok Tin Ind. Ctr., 24-26 Pak Fung St., Kwun Tong, HK China Office : Tel:86-796-85302617 Fax : 86-769-83651274 5-6/F, Rui Kang Building, No. 47 BeiLin Road, Shi Pai Wan Town, Dong Guan City, PRC China Factory Norvik Technology Ltd Tai Lun Technology Ltd Mei Sun Fat (F.S) Silicone Products Co. Ltd Pelvane Technology Ltd Slogan on the name card : We are your best Business Partner With ISO9001 / ISO14001 / TS16949 LOGO Any query, pls contact me at marisodell@qorvent-mail.net Thanks, maris

Reason: Dear All, Still can't choose the right one. Thanks, Maris

Reason: still not confirm

Reason: working on revision. thanks

Reason: revising the design with designer. thanks

Reason: revising with designer ! thanks

Industry/Entity Type

Manufacturer

```html
<!DOCTYPE html>
<html lang="en">
<head>
<meta charset="utf-8">
<title>Qorvent Name Card</title>
<link rel="stylesheet" href="https://fonts.googleapis.com/css2?family=Arimo:wght@400;700&family=Archivo+Black&display=swap">
<style>
  :root {
    --page: #e9e6e1;
    --card: #ffffff;
    --ink: #1c1c1c;
    --ink-soft: #3a3a3a;
    --mark: #2a7fc1;
    --edge: #d8d8d8;
  }
  * { box-sizing: border-box; margin: 0; padding: 0; }
  html, body { width: 1200px; height: 900px; overflow: hidden; background: var(--page); }
  body { position: relative; font-family: "Arimo", Arial, sans-serif; color: var(--ink); }

  .card {
    position: absolute; top: 290px; width: 540px; height: 320px; overflow: hidden;
    background: var(--card); border: 1px solid var(--edge);
    box-shadow: 0 6px 18px rgba(0,0,0,.12);
  }
  .card--front { left: 40px; }
  .card--back { left: 620px; }

  .brand { position: absolute; display: flex; align-items: center; gap: 8px; }
  .brand__dot { width: 26px; height: 26px; border-radius: 50%; background: var(--mark); }
  .brand__name { font-weight: 700; font-size: 24px; line-height: 1; color: var(--ink); }
  .brand__sub { display: block; font-weight: 400; font-size: 8px; letter-spacing: 1px; margin-top: 3px; }

  .slogan { font-size: 17px; font-weight: 700; letter-spacing: .5px; white-space: nowrap; }
  .slogan__best { font-family: "Archivo Black", Arial, sans-serif; font-style: italic; font-weight: 400; }

  /* front */
  .card--front .brand { left: 170px; top: 40px; }
  .factories { position: absolute; left: 0; right: 0; top: 100px; text-align: center; font-size: 16px; line-height: 21px; letter-spacing: .4px; }
  .card--front .slogan { position: absolute; left: 0; right: 0; top: 202px; text-align: center; }
  .standards { position: absolute; left: 0; right: 0; top: 240px; text-align: center; font-size: 11px; letter-spacing: .6px; color: var(--ink-soft); }

  /* back */
  .card--back .brand { right: 30px; top: 22px; }
  .person { position: absolute; left: 30px; top: 68px; }
  .person__name { font-weight: 700; font-size: 26px; letter-spacing: .5px; line-height: 30px; }
  .person__title { font-size: 17px; line-height: 20px; margin-top: 2px; }
  .card--back .slogan { position: absolute; left: 30px; top: 132px; font-size: 14px; letter-spacing: .3px; }

  .office { position: absolute; font-size: 12.5px; line-height: 14.5px; letter-spacing: .3px; }
  .office__head { font-weight: 700; font-size: 14.5px; line-height: 17px; margin-bottom: 2px; }
  .office--hk { left: 50px; top: 164px; }
  .office--cn { left: 330px; top: 72px; }
  .contact { display: flex; align-items: center; gap: 5px; }
  .contact svg { width: 11px; height: 11px; fill: var(--ink); flex: none; }
</style>
</head>
<body>

<section class="card card--front">
  <div class="brand">
    <span class="brand__dot"></span>
    <span class="brand__name">Qorvent<span class="brand__sub">TECHNOLOGY LIMITED</span></span>
  </div>
  <div class="factories">
    <p>Norvik Technology Ltd</p>
    <p>Tai Lun Technology Ltd</p>
    <p>Mei Sun Fat (F.S) Silicone Products Co. Ltd</p>
    <p>Pelvane Technology Ltd</p>
  </div>
  <p class="slogan">We are your <span class="slogan__best">best</span> Business Partner</p>
  <p class="standards">ISO9001 • ISO14001 • ISO/TS16949</p>
</section>

<section class="card card--back">
  <div class="brand">
    <span class="brand__dot"></span>
    <span class="brand__name">Qorvent<span class="brand__sub">TECHNOLOGY LIMITED</span></span>
  </div>

  <div class="office office--cn">
    <p class="office__head">China Office</p>
    <p>5-6/F, Rui Kang Bldg</p>
    <p>No. 47 BeiLin Road,</p>
    <p>Shi Pai Wan Town</p>
    <p>Dong Guan City, PRC</p>
    <p class="contact"><svg viewBox="0 0 12 12"><rect x="3" y="0" width="6" height="12" rx="1"/></svg>86-139-5720 4416</p>
    <p class="contact"><svg viewBox="0 0 12 12"><path d="M1 4c0-2 2-3 5-3s5 1 5 3l-2 1-1-2H4L3 5zM2 6h8l1 5H1z"/></svg>86-796-8530 2617</p>
    <p class="contact"><svg viewBox="0 0 12 12"><rect x="3" y="0" width="6" height="4"/><rect x="0" y="4" width="12" height="8" rx="1"/></svg>86-769-8365 1274</p>
  </div>

  <div class="person">
    <p class="person__name">Maris Odell</p>
    <p class="person__title">Marketing Manager</p>
  </div>
  <p class="slogan">We are your <span class="slogan__best">best</span> Business Partner</p>

  <div class="office office--hk">
    <p class="office__head">Honk Kong Office</p>
    <p>RM705</p>
    <p>7/F, Lok Tin Ind Ctr</p>
    <p>24-26 Pak Fung St</p>
    <p>Kwun Tong, HK</p>
    <p class="contact"><svg viewBox="0 0 12 12"><rect x="3" y="0" width="6" height="12" rx="1"/></svg>852-6483 9205</p>
    <p class="contact"><svg viewBox="0 0 12 12"><path d="M1 4c0-2 2-3 5-3s5 1 5 3l-2 1-1-2H4L3 5zM2 6h8l1 5H1z"/></svg>852-2477 6150</p>
    <p class="contact"><svg viewBox="0 0 12 12"><rect x="3" y="0" width="6" height="4"/><rect x="0" y="4" width="12" height="8" rx="1"/></svg>852-2836 4471</p>
  </div>
</section>

</body>
</html>
```